Webdesign mit Grundfarbe Weinrot für allgemeine Steuerberatung
Zielgruppe
Allgemeine Steuerberatung. Zielgruppe ist breit gefächert, allerdings soll die Webseite eher den Jungunternehmer ansprechen.
Aufgabenstellung
Die Grundfarbe sollte weinrot sein.

```html
<!DOCTYPE html>
<html lang="de">
<head>
<meta charset="utf-8">
<title>Steuerberatung Kessler – Leistungen</title>
<link href="https://fonts.googleapis.com/css2?family=PT+Sans:ital,wght@0,400;0,700;1,400&display=swap" rel="stylesheet">
<style>
:root{
  --wine:#6a1116;
  --wine-soft:#a45a5e;
  --wine-light:#c08a8c;
  --ink:#1c1c1c;
  --white:#ffffff;
}
*{margin:0;padding:0;box-sizing:border-box}
html,body{width:667px;height:1200px;overflow:hidden;background:var(--white)}
body{position:relative;font-family:"PT Sans",sans-serif;color:var(--ink)}
.abs{position:absolute}

/* header */
.brand{left:60px;top:30px;display:flex;align-items:center;gap:6px;color:var(--wine);font-weight:700;font-size:15px;line-height:1.05}
.brand-mark{width:12px;height:12px;border-radius:50%;background:var(--wine)}
.brand small{display:block;font-weight:700;font-size:15px}
.nav{right:64px;top:37px;display:flex;font-size:8px;color:var(--wine)}
.nav a{color:inherit;text-decoration:none;padding:0 6px;border-left:1px solid var(--wine-light)}
.nav a:first-child{border-left:none}

/* hero */
.hero{left:0;top:80px}
.hero-text{left:66px;top:182px;color:var(--white)}
.hero-text h1{font-size:18px;font-weight:700;line-height:1}
.hero-text p{font-size:8.5px;line-height:10.5px;margin-top:2px}
.quick{right:0;background:var(--wine);color:var(--white);display:flex;align-items:center;justify-content:center}
.quick-phone{top:178px;width:88px;height:26px;font-size:7.5px;gap:6px}
.quick-mail{top:206px;width:31px;height:25px}

/* services */
.section-title{left:65px;top:288px;font-size:26px;font-weight:700;color:var(--wine)}
.bar{left:65px;width:531px;height:36px;background:var(--wine);color:var(--white);font-weight:700;font-size:9.5px;display:flex;align-items:center;padding-left:12px;gap:10px}
.bar svg{width:14px;height:8px}
.overview{left:83px;top:378px;width:100px}
.overview h3{font-size:9px;font-weight:700;margin-bottom:6px}
.overview li{list-style:none;font-size:5.8px;line-height:7px}
.detail{left:202px;top:375px;width:392px}
.detail h3{font-size:9px;font-weight:700;margin-bottom:4px}
.detail p{font-size:5.5px;line-height:7.4px;margin-bottom:6px}
.detail .block{margin-bottom:8px}

/* footer */
.footer-band{left:0;top:870px}
.kicker{left:60px;top:930px;color:var(--white);font-weight:700;font-size:11px;border-left:1.5px solid var(--white);padding-left:5px;line-height:13px}
.footer-title{left:60px;top:948px;color:var(--white);font-weight:700;font-size:23px}
.address{left:60px;top:1022px;color:var(--white);font-size:5.8px;line-height:7px;width:140px}
.address strong{font-size:7px;line-height:8.5px;display:block}
.address p{margin-top:6px}
.hours{left:212px;top:1020px;color:var(--white);font-size:7.2px;line-height:8.6px;width:150px}
.hours strong{display:block}
.hours em{display:block}
.hours p{margin-top:7px}
.form{left:388px;top:917px;width:229px}
.field{background:var(--white);height:16px;margin-bottom:8px;font-size:4.5px;font-style:italic;padding:5px 8px}
.field.message{height:36px}
.consent{display:flex;gap:5px;color:var(--white);font-size:3.6px;line-height:4.4px;margin-top:2px}
.consent .box{flex:none;width:5px;height:5px;border:0.6px solid var(--white);margin-top:1px}
.captcha{margin-top:8px;width:106px;height:26px;background:#f9f9f9;border:0.5px solid #d3d3d3;display:flex;align-items:center;gap:5px;padding-left:6px;font-size:4.5px}
.captcha .box{width:9px;height:9px;border:0.8px solid #c1c1c1;background:var(--white)}
.send{margin-top:9px;width:57px;height:17px;background:var(--white);color:var(--wine);font-weight:700;font-size:6px;display:flex;align-items:center;justify-content:center}

.legal{top:1176px;font-size:5px}
.copy{left:60px;font-style:italic}
.links{right:52px;font-size:6px}
</style>
</head>
<body>

<header>
  <div class="abs brand"><span class="brand-mark"></span><div>Marlene<small>Kessler</small></div></div>
  <nav class="abs nav">
    <a href="#">Startseite</a><a href="#">Über uns</a><a href="#">Leistungen</a><a href="#">Aktuelles</a><a href="#">Kontakt</a>
  </nav>
</header>

<svg class="abs hero" width="667" height="200" viewBox="0 0 667 200" role="img" aria-label="Foto eines Taschenrechners mit Stift auf Zahlentabellen, weinrot eingefärbt">
  <defs>
    <linearGradient id="heroTone" x1="0" y1="0" x2="1" y2="1">
      <stop offset="0" stop-color="#9a4e53"/>
      <stop offset="0.5" stop-color="#a8676a"/>
      <stop offset="1" stop-color="#93484d"/>
    </linearGradient>
  </defs>
  <polygon points="0,36 667,8 667,200 0,200" fill="url(#heroTone)"/>
</svg>

<div class="abs hero-text">
  <h1>Unsere Leistungen für</h1>
  <p>Selbstständige | Gewerbe | Existenzgründer<br>Arbeitnehmer<br>Sonstige Einkünfte</p>
</div>

<div class="abs quick quick-phone">
  <svg width="9" height="9" viewBox="0 0 24 24"><path fill="#fff" d="M6.6 10.8a15.1 15.1 0 0 0 6.6 6.6l2.2-2.2a1 1 0 0 1 1-.25 11.4 11.4 0 0 0 3.6.57 1 1 0 0 1 1 1V20a1 1 0 0 1-1 1A17 17 0 0 1 3 4a1 1 0 0 1 1-1h3.5a1 1 0 0 1 1 1c0 1.25.2 2.45.57 3.57a1 1 0 0 1-.25 1z"/></svg>
  <span>0123-456780</span>
</div>
<div class="abs quick quick-mail">
  <svg width="11" height="8" viewBox="0 0 22 16"><rect x="1" y="1" width="20" height="14" fill="none" stroke="#fff" stroke-width="1.6"/><polyline points="1,1 11,9 21,1" fill="none" stroke="#fff" stroke-width="1.6"/></svg>
</div>

<main>
  <h2 class="abs section-title">Unsere Leistungen für...</h2>

  <div class="abs bar" style="top:333px">
    <svg viewBox="0 0 14 8"><polyline points="1,7 7,1 13,7" fill="none" stroke="#fff" stroke-width="1.2"/></svg>
    Selbstständige, Gewerbe und Existenzgründer
  </div>

  <aside class="abs overview">
    <h3>Überblick:</h3>
    <ul>
      <li>» Buchhaltung</li>
      <li>» Lohnabrechnungen</li>
      <li>» Jahresabschluss</li>
      <li>» Steuererklärungen</li>
    </ul>
  </aside>

  <article class="abs detail">
    <div class="block">
      <h3>Buchhaltung für Selbstständige und Gewerbe</h3>
      <p>Wir kontieren und verbuchen Ihre Unterlagen und erstellen die Umsatzsteuervoranmeldungen und Betriebswirtschaftlichen Auswertungen. Dies schließt bei Bedarf die Offene-Posten-Buchhaltung und Anlagenbuchhaltung mit ein.</p>
      <p>Bei Lieferungen und sonstigen Leistungen innerhalb der Europäischen Gemeinschaft kümmern wir uns um die notwendige Zusammenfassende Meldung an das Zentralamt für Steuern.</p>
      <p>Sofern Ihre Buchhaltung als Jahresbuchhaltung (ohne monatliche oder vierteljährliche Umsatzsteuervoranmeldungen) von uns zu bearbeiten ist, unterstützen wir Sie natürlich auch bei Ihren Fragen während des Jahres.</p>
      <p>Wir leisten Hilfestellung für selbstbuchende Mandanten, helfen bei der Gestaltung eines sinnvollen Kostenplanes und Fragen rund um die Verbuchung Ihrer Geschäftsvorfälle.</p>
    </div>
    <div class="block">
      <h3>Lohnabrechnungen für Arbeitgeber</h3>
      <p>Wir erstellen die Lohnabrechnungen für Ihre Arbeitnehmer, gleich ob ein Festgehalt oder Stundenlöhne gezahlt werden, dies schließt die notwendigen Sozialversicherungsmeldungen, Beitragsmeldungen am die Krankenkassen und die Berufsgenossenschaft, sowie die Lohsteueranmeldungen ein. Ebenso kümmern wir uns um die Anträge auf Erstattungen der Lohnfortzahlungen im Krankheitsfall oder bei Mutterschutz. Sie erhalten von uns im Vorfeld einer Beschäftigung (z.B. für Aushilfen) die notwendigen Informationen und Unterlagen. Für Branchen bei denen Sofortmeldungen für neue Arbeitnehmer erfolgen müssen, kümmern wir uns hierum (z.B. Gastronomie, Baugewerbe etc.). Wir kümmern uns um die turnusmäßig stattfindenden Prüfungen der Deutschen Rentenversicherung.</p>
    </div>
    <div class="block">
      <h3>Existenzgründer und Studenten</h3>
      <p>Wir begleiten und unterstützen Sie bei der Aufnahme einer selbstständigen Tätigkeit oder der Neueröffnung eines Gewerbes.</p>
      <p>Dies umfasst die notwendigen Unterlagen zur steuerlichen Erfassung und Hilfestellung zu Beginn, wie z.B. die Beratung, welche Ausgaben sich steuerlich wie auswirken und welche Aufzeichnung notwendig und sinnvoll sind.</p>
      <p>Daneben informieren wir Sie von Anfang an, welche Formalien zu beachten sind, so erläutern wir Ihnen z.B., welche Vorschriften für Rechnungen, die Sie erhalten oder erstellen, gelten und was hinsichtlich der Aufbewahrung von Geschäftsunterlagen zu beachten ist.</p>
    </div>
    <div class="block">
      <h3>Betriebsprüfung bei Unternehmen</h3>
      <p>Wir begleiten Sie bei Betriebsprüfungen durch das Finanzamt oder die Krankenkassen.</p>
      <p>Die Prüfungen finden in der Regel bei uns (nicht in Ihren Räumen) statt, so dass die meisten Klärungsfragen bereits während der Prüfung von uns beantwortet werden können und Sie in Ihrer laufenden Geschäftstätigkeit während der Prüfungsdauer nicht beeinträchtigt werden.</p>
    </div>
  </article>

  <div class="abs bar" style="top:770px">
    <svg viewBox="0 0 14 8"><polyline points="1,1 7,7 13,1" fill="none" stroke="#fff" stroke-width="1.2"/></svg>
    Arbeitnehmer
  </div>
  <div class="abs bar" style="top:816px">
    <svg viewBox="0 0 14 8"><polyline points="1,1 7,7 13,1" fill="none" stroke="#fff" stroke-width="1.2"/></svg>
    Sonstige Einkünfte
  </div>
</main>

<footer>
  <svg class="abs footer-band" width="667" height="295" viewBox="0 0 667 295"><polygon points="0,36 667,0 667,262 0,292" fill="var(--wine)"/></svg>
  <div class="abs kicker">Kontakt</div>
  <h2 class="abs footer-title">So erreichen Sie uns</h2>

  <div class="abs address">
    <strong>Steuerberatung Kessler<br>Dipl. Betriebswirtin (FH)<br>Marlene Kessler Steuerberaterin</strong>
    <p>Lindenweg 12<br>35000 Mittelstadt</p>
    <p>Telefon: 0123-456780<br>Telefax: 0123-456789<br>E-Mail: info@stb-kessler.de</p>
  </div>

  <div class="abs hours">
    <strong>Öffnungszeiten:</strong>
    <em>Mo - Do</em>08:00 - 16:00 Uhr
    <p><em>Fr</em>08:00 - 12:30 Uhr</p>
    <p>Termine sind bei Bedarf natürlich auch außerhalb der üblichen Bürozeiten möglich.</p>
  </div>

  <form class="abs form">
    <div class="field">Name*</div>
    <div class="field">E-Mail*</div>
    <div class="field">Telefon*</div>
    <div class="field message">Nachricht</div>
    <div class="consent"><span class="box"></span><span>Ich habe die <b>Datenschutzerklärung</b> zur Kenntnis genommen. Ich stimme zu, dass meine Angaben und Daten zur Beantwortung meiner Anfrage elektronisch erhoben und gespeichert werden. Hinweis: Sie können Ihre Einwilligung jederzeit für die Zukunft per E-Mail an info@stb-kessler.de widerrufen*</span></div>
    <div class="captcha"><span class="box"></span>Ich bin kein Roboter.</div>
    <div class="send">» senden</div>
  </form>

  <div class="abs legal copy">© 2019 Steuerberatung Kessler</div>
  <div class="abs legal links">Impressum | Datenschutz</div>
</footer>

</body>
</html>
```